Lumora business card for a plastic surgeon

we need a business card for plastic surgeons that work on a clinic called LUMORA.
we want a clean design and the following informations: name of the doctor, doctor's registration number (called CRM), telephone, address, facebook, instagram.
Colors: white, blue tones, light brown/ coffee

facebook and instagram: lumoracirurgiaestetica

Industry/Entity Type

Business

Contact Information for Business Card

clean design

Font styles to use
Serif
Sans Serif
Other font styles liked:
• helvetica light

Colors
cee9f5
85cae6
85abd2
3276b5
cfeae6
cedeed
eaf1f7

Requirements
Must have
• doctor's name
• identification number (called CRM)
• contact (phone, facebook, instagram, address)

```html
<!DOCTYPE html>
<html lang="pt">
<head>
<meta charset="utf-8">
<title>Lumora — Cartão de visita</title>
<link rel="stylesheet" href="https://fonts.googleapis.com/css2?family=Cinzel:wght@400;500&family=Open+Sans:wght@300;400&display=swap">
<style>
  :root {
    --page: #e6edf4;
    --card-top: #22375a;
    --card-bottom: #162740;
    --cyan: #3fb3d8;
    --sky: #85cae6;
    --coffee: #b79877;
    --muted: #8ea3bb;
    --light: #cbd7e4;
    --motif-light: #e3eaf1;
    --motif-mid: #a9bbcf;
    --motif-deep: #7f97b2;
  }
  * { margin: 0; padding: 0; box-sizing: border-box; }
  html, body { width: 793px; height: 1200px; overflow: hidden; }
  body {
    background: var(--page);
    position: relative;
    font-family: "Open Sans", Arial, sans-serif;
  }
  .card {
    position: absolute;
    width: 543px;
    height: 309px;
    background: linear-gradient(160deg, var(--card-top), var(--card-bottom));
    border-radius: 2px;
    box-shadow: 0 8px 24px rgba(22, 39, 64, 0.25);
    overflow: hidden;
  }
  .card--front { left: 128px; top: 147px; }
  .card--back { left: 129px; top: 756px; }

  .motif {
    position: absolute;
    background: linear-gradient(200deg, var(--motif-light) 0%, var(--motif-mid) 55%, var(--motif-deep) 100%);
    opacity: 0.85;
  }
  .card--front .motif { left: 352px; top: 44px; width: 191px; height: 265px; border-top-left-radius: 120px 90px; }
  .card--back .motif { left: 0; top: 0; width: 195px; height: 309px; border-top-right-radius: 120px 90px; }

  .crm {
    position: absolute; right: 46px; top: 18px;
    font-size: 11px; color: var(--coffee); letter-spacing: 0.3px;
  }
  .brand-name {
    position: absolute; left: 30px; top: 34px;
    font-family: "Cinzel", Georgia, serif; font-weight: 400;
    font-size: 54px; line-height: 1; letter-spacing: 2px;
    color: var(--cyan);
  }
  .brand-line {
    position: absolute; left: 42px; top: 100px;
    font-family: "Cinzel", Georgia, serif; font-weight: 400;
    font-size: 19px; letter-spacing: 1px; color: var(--coffee);
  }
  .doctor-name {
    position: absolute; left: 30px; top: 145px;
    font-family: "Cinzel", Georgia, serif; font-weight: 500;
    font-size: 20px; color: var(--cyan); letter-spacing: 0.5px;
  }
  .doctor-role {
    position: absolute; left: 30px; top: 176px;
    font-size: 11px; color: var(--muted); letter-spacing: 0.5px;
  }
  .divider {
    position: absolute; left: 30px; top: 201px;
    width: 252px; height: 1px; background: var(--cyan); opacity: 0.8;
  }
  .contact-list {
    position: absolute; list-style: none;
    font-size: 12.5px; color: var(--muted);
  }
  .card--front .contact-list { left: 30px; top: 218px; }
  .contact-list li { display: flex; align-items: center; height: 22px; }
  .contact-list .address { margin-top: 8px; }
  .icon { width: 13px; height: 13px; margin-right: 11px; flex: none; }
  .icon--square { background: var(--muted); border-radius: 2px; }

  .card--back .contact-list {
    left: 277px; top: 119px;
    font-size: 13px; color: var(--light);
  }
  .card--back .contact-list li { height: 23px; }
  .card--back .icon--square { background: var(--sky); }
</style>
</head>
<body>
  <section class="card card--front" aria-label="Frente do cartão">
    <div class="motif" role="img" aria-label="Área recortada transparente da forma decorativa da marca"></div>
    <p class="crm">CRM 123 456 789</p>
    <h1 class="brand-name">LUMORA</h1>
    <p class="brand-line">CIRURGIA PLÁSTICA</p>
    <h2 class="doctor-name">Dr. Marco Vidal</h2>
    <p class="doctor-role">DIRECTOR</p>
    <div class="divider"></div>
    <ul class="contact-list">
      <li>
        <svg class="icon" viewBox="0 0 13 13" aria-hidden="true">
          <rect width="13" height="13" rx="2" fill="#8ea3bb"/>
          <path d="M4 3.2l1.4 1.6-.7 1c.5 1 1.2 1.7 2.2 2.2l1-.7 1.6 1.4-.8 1.1C6.4 9.6 3.4 6.6 3.2 4z" fill="#1d3050"/>
        </svg>
        210-555-0147
      </li>
      <li><span class="icon icon--square"></span>@lumoracirurgiaestetica</li>
      <li class="address">4820 FAIRVIEW RD., SUITE B. AUSTIN, TX. 78731</li>
    </ul>
  </section>

  <section class="card card--back" aria-label="Verso do cartão">
    <div class="motif" role="img" aria-label="Área recortada transparente da forma decorativa da marca"></div>
    <ul class="contact-list">
      <li>
        <svg class="icon" viewBox="0 0 14 14" aria-hidden="true">
          <circle cx="7" cy="7" r="6.3" fill="none" stroke="#85cae6" stroke-width="1.3"/>
          <ellipse cx="7" cy="7" rx="2.8" ry="6.3" fill="none" stroke="#85cae6" stroke-width="1.1"/>
          <path d="M1 7h12M2 4h10M2 10h10" stroke="#85cae6" stroke-width="1"/>
        </svg>
        www.lumoracirurgiaestetica.com
      </li>
      <li><span class="icon icon--square"></span>/lumoracirurgiaestetica</li>
      <li><span class="icon icon--square"></span>#lumoracirurgiaestetica</li>
    </ul>
  </section>
</body>
</html>
```